Hot young IT advisor needs business cards as upscale and innovative as they are

We need business cards that make a statement about who we are, as a young and upscale IT advisor. Our whole angle is innovation and tenacity in our personal relationships with our clients. We've just done a brand overhaul and need cards that have the new logos, but we're also looking for someone with a sixth sense who can capture what sets us apart and communicate that with a business card. Clean, minimalist, upscale, innovative, personal. Our budget only allows room for them to be soft-touch, no spot gloss or foil designs please.

Target Market(s)

High-level decision makers at middle-market and large organizations in the healthcare, financial services, sports and entertainment, K-12 education, college and university, state and local government, and federal government sectors.

Industry/Entity Type

Information Technology

Font styles to use
Sans Serif

Colors
ec1f27
606060
ffffff

Requirements
Should not have
• Designs with low contrast which would require spot-gloss or embossing.

```html
<!DOCTYPE html>
<html lang="en">
<head>
<meta charset="utf-8">
<title>Norvale – Business Cards</title>
<link rel="stylesheet" href="https://fonts.googleapis.com/css2?family=Montserrat:wght@500;600&family=Roboto:wght@400&display=swap">
<style>
  :root {
    --brand-red: #ec1f27;
    --ink-grey: #606060;
    --ink-dark: #3a3a3a;
    --paper: #ffffff;
    --stage: #e9e9e9;
    --rule: #d4d4d4;
    --faint-dot: #e6e6e6;
  }
  * { margin: 0; padding: 0; box-sizing: border-box; }
  html, body {
    width: 1200px;
    height: 976px;
    overflow: hidden;
    background: var(--stage);
  }
  .canvas {
    position: relative;
    width: 1200px;
    height: 976px;
  }
  .card {
    position: absolute;
    width: 560px;
    height: 320px;
    background: var(--paper);
    box-shadow: 0 6px 18px rgba(0,0,0,0.18);
    overflow: hidden;
  }
  .card--front { left: 60px; top: 90px; }
  .card--back { left: 580px; top: 566px; }

  /* brand wordmark */
  .brand {
    position: absolute;
    display: flex;
    align-items: center;
    gap: 10px;
    font-family: "Montserrat", sans-serif;
    font-weight: 600;
    color: var(--brand-red);
    letter-spacing: 0.12em;
  }
  .brand__square {
    width: 16px;
    height: 16px;
    background: var(--brand-red);
  }
  .card--front .brand {
    left: 128px;
    top: 98px;
    font-size: 28px;
  }
  .card--back .brand {
    left: 50%;
    top: 50%;
    transform: translate(-50%, -50%);
    font-size: 34px;
  }
  .card--back .brand__square { width: 20px; height: 20px; }

  /* corner dot field, shown as soft tone */
  .dot-field {
    position: absolute;
    top: 0;
    right: 0;
    width: 120px;
    height: 170px;
    clip-path: polygon(0 0, 100% 0, 100% 100%, 35% 70%);
  }
  .card--front .dot-field {
    background: linear-gradient(180deg, rgba(236,31,39,0.55) 0%, rgba(236,31,39,0.35) 60%, rgba(96,96,96,0.45) 100%);
  }
  .card--back .dot-field {
    background: linear-gradient(180deg, var(--faint-dot) 0%, #f1f1f1 100%);
  }

  /* holder */
  .holder {
    position: absolute;
    left: 46px;
    bottom: 56px;
    font-family: "Montserrat", sans-serif;
  }
  .holder__name {
    font-size: 22px;
    font-weight: 500;
    color: var(--ink-dark);
    letter-spacing: 0.02em;
  }
  .holder__role {
    font-size: 12px;
    font-weight: 500;
    color: var(--brand-red);
    letter-spacing: 0.04em;
    margin-top: 2px;
  }

  .divider {
    position: absolute;
    left: 318px;
    top: 170px;
    width: 1px;
    height: 80px;
    background: var(--rule);
  }

  .contact {
    position: absolute;
    left: 336px;
    top: 174px;
    list-style: none;
    font-family: "Roboto", sans-serif;
    font-size: 12.5px;
    color: var(--ink-dark);
  }
  .contact__item {
    display: flex;
    align-items: center;
    gap: 8px;
    height: 24px;
  }
  .contact__icon { width: 11px; height: 11px; flex: none; }
</style>
</head>
<body>
<main class="canvas">

  <section class="card card--front" aria-label="Business card front">
    <div class="dot-field" role="img" aria-label="Corner pattern of red and grey dots"></div>

    <div class="brand">
      <span class="brand__square"></span>
      <span class="brand__name">NORVALE</span>
    </div>

    <div class="divider"></div>

    <ul class="contact">
      <li class="contact__item">
        <svg class="contact__icon" viewBox="0 0 12 12" aria-hidden="true">
          <path d="M2.5 1 L4.5 1 L5.3 3.6 L4 4.6 C4.7 6.1 5.9 7.3 7.4 8 L8.4 6.7 L11 7.5 L11 9.5 C11 10.3 10.3 11 9.5 11 C5 11 1 7 1 2.5 C1 1.7 1.7 1 2.5 1 Z" fill="var(--brand-red)"/>
        </svg>
        <span>+0000 289 8165</span>
      </li>
      <li class="contact__item">
        <svg class="contact__icon" viewBox="0 0 12 12" aria-hidden="true">
          <rect x="0.5" y="2" width="11" height="8" fill="var(--brand-red)"/>
          <path d="M0.8 2.4 L6 6.6 L11.2 2.4" fill="none" stroke="#fff" stroke-width="1"/>
        </svg>
        <span>info@companyname.com</span>
      </li>
      <li class="contact__item">
        <svg class="contact__icon" viewBox="0 0 12 12" aria-hidden="true">
          <circle cx="6" cy="6" r="5.5" fill="var(--brand-red)"/>
          <path d="M0.8 6 H11.2 M6 0.8 C3.8 3.5 3.8 8.5 6 11.2 M6 0.8 C8.2 3.5 8.2 8.5 6 11.2" fill="none" stroke="#fff" stroke-width="0.8"/>
        </svg>
        <span>www.companyname.com</span>
      </li>
    </ul>

    <div class="holder">
      <p class="holder__name">JOHN DOE</p>
      <p class="holder__role">DESIGNATION</p>
    </div>
  </section>

  <section class="card card--back" aria-label="Business card back">
    <div class="dot-field" role="img" aria-label="Faint corner pattern of grey dots"></div>
    <div class="brand">
      <span class="brand__square"></span>
      <span class="brand__name">NORVALE</span>
    </div>
  </section>

</main>
</body>
</html>
```